Industrial Laundry News Paper Add

We need a color add for 1/4 page newspaper using blue and white. We are an industrial laundry providing linen washing for condo rental companies. We can provide linen rental and wash customer-owned goods

```html
<!DOCTYPE html>
<html lang="en">
<head>
<meta charset="utf-8">
<title>Summit Ridge Services – Industrial Laundry Ad</title>
<link href="https://fonts.googleapis.com/css2?family=Montserrat:wght@300;400;500;600;700&display=swap" rel="stylesheet">
<style>
  :root {
    --page-bg: #5a5a5a;
    --navy: #1a1c66;
    --royal: #2f4fa2;
    --ink: #2a2a33;
    --white: #ffffff;
    --paper: #f6f6f8;
    --steel-1: #d8d9dc;
    --steel-2: #a9abaf;
    --steel-3: #7d7f84;
    --steel-4: #5b5d62;
    --steel-5: #3f4145;
  }
  * { margin: 0; padding: 0; box-sizing: border-box; }
  html, body {
    width: 1200px; height: 2400px; overflow: hidden;
    background: var(--page-bg);
    font-family: "Montserrat", sans-serif;
  }
  .ad {
    position: absolute;
    left: 60px; top: 501px;
    width: 950px; height: 1230px;
    transform: scale(1.1368);
    transform-origin: top left;
    background: var(--paper);
    overflow: hidden;
    box-shadow: 0 20px 40px rgba(0,0,0,.35);
  }
  .ad-photo {
    position: absolute; left: 0; top: 0; width: 950px; height: 700px;
    background: linear-gradient(100deg,
      var(--steel-3) 0%, var(--steel-2) 14%, var(--steel-4) 26%,
      var(--steel-2) 40%, var(--steel-1) 50%, var(--steel-3) 60%,
      var(--steel-2) 72%, var(--steel-1) 82%, var(--steel-3) 92%, var(--steel-4) 100%);
  }
  .ad-shapes { position: absolute; left: 0; top: 0; width: 950px; height: 1230px; }
  .headline { position: absolute; left: 73px; top: 738px; color: var(--navy); }
  .headline-lead { font-weight: 300; font-size: 39px; line-height: 54px; color: var(--ink); }
  .headline-main { font-weight: 600; font-size: 41px; line-height: 54px; }
  .services { position: absolute; list-style: none; font-size: 21px; font-weight: 400; color: var(--ink); }
  .services li { position: relative; padding-left: 25px; }
  .services li::before { content: "✓"; position: absolute; left: 0; top: 0; color: var(--navy); }
  .services-left { left: 73px; top: 870px; }
  .services-left li { line-height: 46px; height: 46px; }
  .services-right { left: 505px; top: 880px; line-height: 30px; }
  .services-right li { margin-bottom: 8px; }
  .brand { position: absolute; left: 530px; top: 668px; width: 345px; text-align: center; }
  .brand-mark { display: block; width: 66px; height: 66px; margin: 0 auto 12px; background: var(--navy); }
  .brand-name { font-weight: 700; font-size: 37px; line-height: 39px; color: var(--navy); letter-spacing: .3px; }
  .brand-tagline { font-weight: 500; font-size: 14px; margin-top: 6px; color: var(--royal); letter-spacing: .2px; }
  .contact { position: absolute; color: var(--white); }
  .contact-left { left: 68px; top: 1104px; font-size: 18px; font-weight: 500; line-height: 23px; }
  .contact-row { display: flex; gap: 10px; align-items: flex-start; }
  .contact-row + .contact-row { margin-top: 19px; }
  .contact-row svg { flex: none; margin-top: 4px; }
  .divider { position: absolute; left: 468px; top: 1110px; width: 2px; height: 78px; background: var(--white); }
  .contact-right { left: 538px; top: 1106px; }
  .phone { display: flex; align-items: center; gap: 12px; font-size: 37px; font-weight: 500; line-height: 46px; }
  .web { display: flex; align-items: center; gap: 12px; font-size: 18px; font-weight: 500; margin-top: 5px; }
</style>
</head>
<body>
  <div class="ad">
    <div class="ad-photo" role="img" aria-label="Photo of a row of stainless steel front-loading industrial washing machines"></div>

    <svg class="ad-shapes" viewBox="0 0 950 1230" aria-hidden="true">
      <path d="M0 560 C 250 700, 600 520, 950 555 L950 1230 L0 1230 Z" fill="var(--paper)"/>
      <path d="M95 410 C 0 470, -10 580, 60 625 C 140 675, 300 640, 520 580 C 700 535, 850 545, 950 555 C 840 540, 690 555, 520 600 C 300 660, 130 690, 40 640 C -20 590, 10 470, 95 410 Z" fill="var(--navy)"/>
      <path d="M140 690 C 330 650, 500 590, 640 600 C 740 605, 810 625, 860 645 C 780 620, 700 610, 620 612 C 480 618, 330 670, 140 690 Z" fill="var(--royal)"/>
      <path d="M0 1050 C 300 1090, 650 1060, 950 950" fill="none" stroke="var(--royal)" stroke-width="2"/>
      <path d="M0 1010 C 250 1080, 650 1070, 950 990 L950 1230 L0 1230 Z" fill="var(--navy)"/>
    </svg>

    <div class="headline">
      <div class="headline-lead">The First Name</div>
      <div class="headline-main">In Industrial Laundry</div>
    </div>

    <ul class="services services-left">
      <li>Commercial Laundry</li>
      <li>Carpet Cleaning</li>
      <li>Housekeeping In Pine Hollow</li>
    </ul>

    <ul class="services services-right">
      <li>Linen washing for condo rental<br>companies</li>
      <li>Linen rental and wash customer<br>-owned goods</li>
    </ul>

    <div class="brand">
      <span class="brand-mark"></span>
      <div class="brand-name">SUMMIT RIDGE<br>SERVICES</div>
      <div class="brand-tagline">HOUSEKEEPING·LAUNDRY·CARPET CLEANING</div>
    </div>

    <div class="contact contact-left">
      <div class="contact-row">
        <svg width="14" height="18" viewBox="0 0 14 18"><circle cx="7" cy="6" r="4.5" fill="none" stroke="#fff" stroke-width="1.6"/><path d="M7 10.5 V16 M3 16 H11" stroke="#fff" stroke-width="1.6"/></svg>
        <div>Granite Peak Partners, Inc.<br>Pine Hollow, CA 93500, USA</div>
      </div>
      <div class="contact-row">
        <svg width="14" height="12" viewBox="0 0 14 12"><rect x="1" y="1" width="12" height="10" fill="none" stroke="#fff" stroke-width="1.4"/><path d="M1 1 L7 6 L13 1" fill="none" stroke="#fff" stroke-width="1.4"/></svg>
        <div>info@summitridgeservices.com</div>
      </div>
    </div>

    <div class="divider"></div>

    <div class="contact contact-right">
      <div class="phone">
        <svg width="34" height="34" viewBox="0 0 34 34"><circle cx="17" cy="17" r="15" fill="none" stroke="#fff" stroke-width="2"/><path d="M12 9 L15 12 L13 15 C14 18 16 20 19 21 L22 19 L25 22 L22 25 C15 24 10 19 9 12 Z" fill="none" stroke="#fff" stroke-width="1.8" stroke-linejoin="round"/></svg>
        <span>+1.5550142300</span>
      </div>
      <div class="web">
        <svg width="18" height="18" viewBox="0 0 18 18"><circle cx="9" cy="9" r="7.5" fill="none" stroke="#fff" stroke-width="1.4"/><ellipse cx="9" cy="9" rx="3.3" ry="7.5" fill="none" stroke="#fff" stroke-width="1.2"/><path d="M1.5 9 H16.5" stroke="#fff" stroke-width="1.2"/></svg>
        <span>www.SummitRidgeServices.com</span>
      </div>
    </div>
  </div>
</body>
</html>
```